Velvet Bloom Marisol's Cleaning Service Business Cards Project

A business card with all contact details with logo design on there (already have a logo) eye catching Logo and contact info on one side, full logo on the back, must target upper class residential and corporate companies, fitness companies, still keep it on the feminine side of things , must look elegant

Target Market(s)

Upper class homes and corporate companies

Industry/Entity Type

Cleaning Service

Contact Information for Business Card

Name: Marisol Denhart
Position: Director
ABN: 47193062857
Email: marisolsvelvetcleaning@brightmail.example
Number: 0418926547

Font styles to use
Decorative

Colors

Designer to choose colors to be used in the design.

Requirements
Must have
• Available Sydney Wide, contact info and logo on one side, full logo on the back
Nice to have
• Professional appearance
Should not have
• Cheap advert looking stuff

```html
<!DOCTYPE html>
<html lang="en">
<head>
<meta charset="utf-8">
<title>Velvet Bloom – Business Cards</title>
<link rel="stylesheet" href="https://fonts.googleapis.com/css2?family=Noto+Serif:wght@700&family=Roboto:wght@400;500&display=swap">
<style>
  :root {
    --backdrop: #3b3b3c;
    --card: #232324;
    --teal: #6ccfcf;
    --white: #f4f4f4;
  }
  * { box-sizing: border-box; margin: 0; padding: 0; }
  html, body {
    width: 1200px; height: 900px; overflow: hidden;
    background: var(--backdrop);
  }
  .sheet {
    position: relative; width: 1200px; height: 900px;
  }
  .card {
    position: absolute; left: 250px; width: 700px; height: 400px;
    background: var(--card);
    box-shadow: 0 10px 30px rgba(0,0,0,.35);
    overflow: hidden;
  }
  .card::after {
    content: ""; position: absolute; left: 0; right: 0; bottom: 0; height: 8px;
    background: var(--teal);
  }
  .card-front { top: 35px; }
  .card-contact { top: 465px; }

  .brand {
    font-family: "Noto Serif", serif; font-weight: 700; color: var(--teal);
    text-align: center; display: flex; flex-direction: column; align-items: center;
  }
  .brand-dot {
    width: 14px; height: 14px; border-radius: 50%; background: var(--teal);
    margin-bottom: 18px;
  }
  .brand-name { font-size: 40px; letter-spacing: 1px; text-transform: uppercase; line-height: 1; }
  .brand-sub { font-size: 12px; letter-spacing: 5px; text-transform: uppercase; margin-top: 10px; }

  .card-front .brand {
    position: absolute; left: 0; right: 0; top: 130px;
  }

  .card-contact .brand {
    position: absolute; left: 20px; width: 280px; top: 140px;
  }
  .card-contact .brand-name { font-size: 28px; }
  .card-contact .brand-sub { font-size: 8.5px; letter-spacing: 3px; }

  .divider {
    position: absolute; left: 318px; top: 110px; width: 2px; height: 190px;
    background: var(--white);
  }
  .details {
    position: absolute; left: 342px; top: 118px; width: 340px;
    font-family: Roboto, sans-serif; color: var(--white);
  }
  .person-name {
    font-family: "Noto Serif", serif; font-weight: 700; color: var(--teal);
    font-size: 28px; line-height: 1.1;
  }
  .person-role { font-size: 17px; margin-top: 4px; }
  .abn { font-size: 18px; margin-top: 26px; }
  .abn-label { color: var(--teal); font-weight: 500; }
  .contact-line { display: flex; align-items: center; gap: 10px; font-size: 17px; margin-top: 14px; }
  .contact-line + .contact-line { margin-top: 6px; }
  .contact-line svg { width: 18px; height: 18px; flex: none; }
  .email { font-size: 14px; white-space: nowrap; }
</style>
</head>
<body>
<main class="sheet">
  <section class="card card-front">
    <div class="brand">
      <span class="brand-dot"></span>
      <span class="brand-name">Velvet Bloom</span>
      <span class="brand-sub">Marisol's Cleaning Service</span>
    </div>
  </section>

  <section class="card card-contact">
    <div class="brand">
      <span class="brand-dot"></span>
      <span class="brand-name">Velvet Bloom</span>
      <span class="brand-sub">Marisol's Cleaning Service</span>
    </div>
    <div class="divider"></div>
    <div class="details">
      <p class="person-name">Marisol Denhart</p>
      <p class="person-role">Director</p>
      <p class="abn"><span class="abn-label">ABN:</span> 47193062857</p>
      <p class="contact-line">
        <svg viewBox="0 0 24 24" aria-hidden="true"><path fill="#6ccfcf" d="M6.6 10.8a15.1 15.1 0 0 0 6.6 6.6l2.2-2.2c.3-.3.7-.4 1-.2 1.1.4 2.3.6 3.6.6.6 0 1 .4 1 1V20c0 .6-.4 1-1 1C10.6 21 3 13.4 3 4c0-.6.4-1 1-1h3.5c.6 0 1 .4 1 1 0 1.3.2 2.5.6 3.6.1.3 0 .7-.2 1z"/></svg>
        <span>0418926547</span>
      </p>
      <p class="contact-line">
        <svg viewBox="0 0 24 24" aria-hidden="true"><rect x="2.5" y="5.5" width="19" height="13" fill="none" stroke="#6ccfcf" stroke-width="1.6"/><path d="M2.5 5.5 12 13l9.5-7.5" fill="none" stroke="#6ccfcf" stroke-width="1.6"/></svg>
        <span class="email">marisolsvelvetcleaning@brightmail.example</span>
      </p>
    </div>
  </section>
</main>
</body>
</html>
```